Willowbend Pharmacy Business Cards

I need a business card design and or template. Needs to convey a softer feel along with health and wellness. Please see attached logo and color scheme.

Industry/Entity Type

Pharmacy

Colors

Designer to choose colors to be used in the design.

Requirements
Must have
• I've added a second NEW colored logo I think I am going to go with the blue green logo.
• Needs to have the colors and feel of the logo attached.
• Dorian Kessel
• Pharmacy Manager
• willowbendpharmacy.example

```html
<!DOCTYPE html>
<html lang="en">
<head>
<meta charset="utf-8">
<title>Willowbend Pharmacy Business Cards</title>
<link rel="stylesheet" href="https://fonts.googleapis.com/css2?family=Montserrat:wght@400;500;600;700&display=swap">
<style>
  :root {
    --sky: #35a3d3;
    --leaf: #9cc43f;
    --slate: #5d6770;
    --ink: #3f4449;
    --paper: #ffffff;
    --backdrop: #e4e7ea;
  }
  * { margin: 0; padding: 0; box-sizing: border-box; }
  html, body { width: 1200px; height: 782px; overflow: hidden; }
  body {
    background: var(--backdrop);
    font-family: "Montserrat", sans-serif;
    position: relative;
  }
  .card {
    position: absolute;
    top: 242px;
    width: 520px;
    height: 297px;
    border-radius: 4px;
    overflow: hidden;
    box-shadow: 0 6px 18px rgba(0,0,0,.15);
  }
  /* Back: contact details */
  .card--details { left: 50px; background: var(--paper); }
  .holder { position: absolute; left: 26px; top: 28px; }
  .holder__name {
    color: var(--sky); font-weight: 700; font-size: 17px;
    text-transform: uppercase; letter-spacing: .3px;
  }
  .holder__title { color: var(--ink); font-size: 12px; margin-top: 3px; }
  .contacts {
    position: absolute; left: 26px; top: 96px; list-style: none;
    color: var(--ink); font-size: 11.5px; line-height: 1.35;
  }
  .contacts li { display: flex; align-items: flex-start; gap: 7px; margin-bottom: 4px; }
  .contacts svg { flex: none; width: 12px; height: 12px; margin-top: 2px; }
  .brand {
    position: absolute; left: 318px; top: 96px;
    display: flex; align-items: center; gap: 10px;
  }
  .brand__dot { width: 30px; height: 30px; border-radius: 50%; background: var(--leaf); flex: none; }
  .brand__name {
    color: var(--slate); font-weight: 700; font-size: 22px; line-height: 1.1;
  }
  .waves { position: absolute; left: 0; top: 0; width: 520px; height: 297px; }
  /* Front: brand side */
  .card--brand { left: 630px; background: var(--sky); }
  .card--brand .brand { left: 0; right: 0; top: 102px; justify-content: center; }
  .card--brand .brand__dot { background: var(--paper); width: 40px; height: 40px; }
  .card--brand .brand__name { color: var(--paper); font-size: 30px; line-height: 1; }
  .site {
    position: absolute; left: 0; right: 0; top: 190px; text-align: center;
    color: var(--paper); font-weight: 600; font-size: 15px; letter-spacing: .4px;
  }
</style>
</head>
<body>

<section class="card card--details">
  <svg class="waves" viewBox="0 0 520 297" aria-hidden="true">
    <path d="M0 172 C120 198 300 238 520 252 V297 H0Z" fill="var(--leaf)"/>
    <path d="M0 192 C130 220 300 254 520 266 V297 H0Z" fill="var(--paper)"/>
    <path d="M0 198 C130 228 300 262 520 274 V297 H0Z" fill="var(--sky)"/>
  </svg>

  <div class="holder">
    <p class="holder__name">Dorian Kessel</p>
    <p class="holder__title">Pharmacy Manager</p>
  </div>

  <ul class="contacts">
    <li>
      <svg viewBox="0 0 12 12"><path d="M3 1 L5 3.5 L4 4.8 C4.8 6.5 5.6 7.3 7.2 8 L8.5 7 L11 9 L9.8 11 C5 10.5 1.5 7 1 2.2Z" fill="var(--sky)"/></svg>
      <span>360-555-0147</span>
    </li>
    <li>
      <svg viewBox="0 0 12 12"><rect x="1" y="2.5" width="10" height="7" rx="1" fill="var(--sky)"/><path d="M1.5 3 L6 6.5 L10.5 3" stroke="#fff" fill="none" stroke-width="1"/></svg>
      <span>dorian@willowbendpharmacy.example</span>
    </li>
    <li>
      <svg viewBox="0 0 12 12"><circle cx="6" cy="6" r="5" fill="var(--sky)"/><path d="M1 6 H11 M6 1 C3.5 4 3.5 8 6 11 M6 1 C8.5 4 8.5 8 6 11" stroke="#fff" fill="none" stroke-width=".8"/></svg>
      <span>www.willowbendpharmacy.example</span>
    </li>
    <li>
      <svg viewBox="0 0 12 12"><path d="M6 11.5 C3 8 2 6.2 2 4.5 A4 4 0 0 1 10 4.5 C10 6.2 9 8 6 11.5Z" fill="var(--sky)"/><circle cx="6" cy="4.5" r="1.5" fill="#fff"/></svg>
      <span>218 Alder Grove Rd.<br>Maple Falls, WA., 98266</span>
    </li>
  </ul>

  <div class="brand">
    <span class="brand__dot"></span>
    <p class="brand__name">Willowbend<br>Pharmacy</p>
  </div>
</section>

<section class="card card--brand">
  <div class="brand">
    <span class="brand__dot"></span>
    <p class="brand__name">Willowbend Pharmacy</p>
  </div>
  <p class="site">www.willowbendpharmacy.example</p>
</section>

</body>
</html>
```